Web Design Peartreegrove

Overview: To develop web site with 1 main page and 1 sample inside page. Site already exists, but has been put offline. Content has been fully rewritten. If I like your style, I will pay extra for additional inside pages.
WHO I AM?
www.peartreegrove.example was originally created to become an online community for people to use my online tools, researches, and findings to learn how to become happier.
Today, my primary services is “health coaching and lifestyle specialist.” I’m a food specialist suggesting customized solutions for my clients to eat better, how to eat, cook, groceries shop, lose weight, reduce craving, and reverse diseases.
My edge is when a suggest food I explain Why such food hurts them (or make them sick –or reason of diseases) or how the food I suggest can heal them, strengthen them, or make them lose weight. My connection to food is medical and directly impacts my client’s health.
I want to be seen as a professional in clinical nutrition and as a guru in overall wellbeing.
I coach my clients’ lifestyle as a WHOLE, introducing them to new food, fitness, and teaching them techniques to better cope with life. I study their overall health, history, and treatments, diseases, allergies as a WHOLE, connecting all medical specialties.
My services:
I sell coaching sessions, for 1 hour, 2/month for a total program of 6 months. During the sessions, I not only coach client on nutrition, but also on career, relationship, fitness, goals, and the reasons why people can’t achieve their dreams, or how to remove stress or re-organize their lives.
Future services: I may want to sell products such as T-shirts and other promotional items
Payment methods: Since I sell, I’ll need coinlatch and credit card payment on line. I accept checks as well (they can find my address on “contact us”)
More services, near future:
As a Certified personal fitness Trainer, I will soon offer circuit training (outdoors) and boot camps in the neighborhood to get people moving, at very affordable prices. The goal of those events will be to grow my peartreegrove community and get new clients for Health coaching.
Knowledgeable about controlling the mind, anger, and stress, I will soon offer group meditations and breathing sessions .
Objectives:
The goal of the site are:
• To entice visitors to become my clients. The look of the site needs to reflect my customized services.
• To offer to spend an hour with client for a free health history.
• To post videos about cooking videos, discussing a theme (sugar craving, which Carbs is good for me?)
• After I meet people and give them my business cards, as they visit my site, they needs to feel impressed by the caliber of expertise.
Schedules and Budget:
Target due date is 1 week from submission of my project. During that phase, I’d like to see a wireframe, colors, styles, incorporating my logo, suggesting pictures. I would like designed tabs, access to videos, and photo library.
Motivations for people to become CLIENTS:
I think what would make people want to get my services is if they see me as an expert in holistic weight loss, someone that they can share their life, thrust, and speak at length without being judged. Visuals are crucial to simply explain effect of food on the body (needs videos main page and archive videos on various topics)
Overall, the emotions we can play with - (key words) feeling energized, feeling strong, in control of your life, a holitistic approach to a new healthy lifestyle, Balance mind, fitness, and diet, take responsibility for your own life, feeling lighter, happier, more peaceful.
Key issues of my clients:
Weight issues, high blood pressure, depression, anxiety, stress, don’t know and what to cook, suffer from diabetes, celiac, digestive diseases. People are fatigued or can’t sleep. They are addicted to sugar, coffee, fast food, speedy life.
Another issue is finding time to eat better, making exercise a routine, making the time to remove stress and enjoy life.
How do I solve clients’ problems?:
Rather than being treated by various medical specialists, I look over their Overall health since childhood. I try to find triggers of their sicknesses that often originate from their lifestyle (stress, lack of exercise, eating junk, allergies) and I recommend life modification, introduce new food, exercise , and help them shuffle their lives around. My approach is extremely customized and always requires Hours of research on my side to fully guide a client.
Demographics:
Teenagers, singles, families, young mothers. Most of clients come with weight issues, some may come to reduce cravings.
Key Messages:
The main page (please find attached “wireframe”) shall give the visitor a sense he found the guru in holistic health. Whatever medical concern they have or struggle will finally be taken care of. Someone loves them and truly cares. Food knowledge is medical, flavor, and based on client’s own taste and willingness to try. The overall feel needs to be sleek and professional.
Call to Action
Ideally, I want people to e-mail me their filled up health history (can download blank men or women health history form) so I can schedule an appointment with them (the best solution for me)
People can also call me. Since calling me is for general questions about my program, I would prefer the e-mail version whereby clients send me their health history.
Creative Considerations
Layout – considerations in accordance to brand guidelines
Need suggetions!
Tone –
Expert in clinical food and holistic health.
Visual
Color palette : I’m not sure, but the background could be light gray (clinical health), golden desert, sahara desert, earthy, pottery (well being) warm colors (orange to warm brown) or other suggestion?
Photography: I thought about flash picture. 1 picture as banner with a message on it. About 3 pictures rotate randomly.
Picture A: is “holistic food, green vegetables, natural edible roots, or cruciferous vegetables, a platter of fresh fruits and vegies, or fresh market (spices, roots, fruits and vegies). Picture needs to be crisp clear.
Picture B: Ideally: a lady fitness trainer training group exercise outdoors, in a park, or a group of people exercising outside, people look happy, boot camp training, circuit training as a group
Picture C: a picture representing the soul ,meditation, a person relaxing next to beach or in forest, next to flowers or lushy plants, a person re-energizing.
Logo: attached as separate files with various backgrounds
Icons: may look cool to use vegies or weight, happy face, or ginger root…
typography, graphics: need suggestions!

Resources
• I have an existing website name “peartreegrove.example” the site has been put out of internet since we were trying to change it. Let me know if you need to access site. Content of the site is ineffective.
• All content has been written. You can suggest layouts and tabs
Updates

Target Market(s)

My industry is Health care, holistic Health (no medications, no supplements, no surgeries)
Buyer’s Type could be anyone wanting to lose weight, feel better, reduce stress, learn to eat, to cook, to groceries shop. My buyers are confused about all diets.My audience is people WHO WANT change in their lives. Some people know they should eat better, they mostly need support and motivation.
Typical buyer is someone who wants a new chance, a new life!
My primary target buyer is:
1. Family. I wish to coach the entire family into healthier eating and teach them how to cook and eat as a family by changing their habits.
My secondary markets are:
1.Teenagers (often eating emotionally and confused about diets)

Industry/Entity Type

Requirements
Must have
• • Format – web, print, video, sound
I would like videos (clipvane connect) – friendloom connect – calendar (I will update) – I will update my content, videos, and photo library regularly – people should be able to e-mail me from site – maybe be able to go through web conference. 2 different words or pdf forms shall be available for download or online filling, then they should be able to e-mail forms through site or through their personal mail system. They can also print and mail it to me.
Managing the site:
I would like to upload videos, pictures and text freely and easily. I would like to manage and update content
Nice to have
• would look cool to use entire background as a super picture!

```html
<!DOCTYPE html>
<html lang="en">
<head>
<meta charset="utf-8">
<title>Peartreegrove – Balanced Nutrition, Mind, and Fitness</title>
<link rel="stylesheet" href="https://fonts.googleapis.com/css2?family=Open+Sans:wght@400;600&family=Ropa+Sans&display=swap">
<style>
:root{
  --green:#5a9a2e;
  --green-dark:#3f7d1f;
  --orange:#f07a1a;
  --orange-light:#f7a14a;
  --text:#444;
  --text-soft:#666;
  --heading:#222;
  --line:#dcdcdc;
  --panel:#f4f4f4;
  --white:#fff;
}
*{box-sizing:border-box;margin:0;padding:0}
html,body{width:1004px;height:1200px;overflow:hidden;background:var(--white)}
body{position:relative;font-family:"Open Sans",Arial,sans-serif;color:var(--text)}
.head-font{font-family:"Ropa Sans","Open Sans",sans-serif}
.top-band{position:absolute;left:0;top:0;width:1004px;height:7px;background:var(--green)}

.brand{position:absolute;left:18px;top:48px;display:flex;align-items:center;gap:10px}
.brand-mark{width:64px;height:64px;border-radius:50%;background:var(--green)}
.brand-name{font-family:"Ropa Sans",sans-serif;font-size:36px;color:var(--green-dark);line-height:1}
.brand-tagline{font-size:9px;letter-spacing:.6px;color:#333;margin-top:4px;font-weight:600}

.search{position:absolute;left:772px;top:36px;width:198px;height:25px;background:#eee;border-radius:4px;display:flex;align-items:center;justify-content:space-between;padding:0 8px;font-size:11px;color:#888}

.main-nav{position:absolute;left:411px;top:80px;width:566px;height:66px;display:flex;background:linear-gradient(var(--orange-light),var(--orange));border-radius:4px 4px 0 0}
.main-nav a{font-family:"Ropa Sans",sans-serif;color:var(--white);text-decoration:none;font-size:17px;line-height:18px;padding:14px 10px 0 17px;border-right:1px solid rgba(255,255,255,.4)}
.main-nav a:last-child{border-right:0}

.hero{position:absolute;left:8px;top:154px;width:700px;height:312px;border-radius:4px;overflow:hidden;
  background:linear-gradient(160deg,#8dbfe6 0%,#6fa6cf 55%,#b9c2c4 100%)}
.hero-caption{position:absolute;left:0;bottom:0;width:100%;height:40px;background:rgba(60,50,40,.7);display:flex;align-items:center;justify-content:space-between;padding:0 12px 0 20px;color:var(--white);font-size:18px}
.hero-dots{display:flex;gap:4px}
.hero-dots span{width:11px;height:11px;border-radius:50%;background:#aaa}
.hero-dots span:first-child{background:var(--white)}

.promo{position:absolute;left:714px;width:269px;height:155px;border:1px solid var(--line);border-radius:4px;overflow:hidden;background:var(--white)}
.promo-photo{position:absolute;right:0;top:0;width:110px;height:100%}
.promo-body{position:absolute;left:15px;top:14px;width:160px}
.promo-title{font-family:"Ropa Sans",sans-serif;color:var(--orange);font-size:21px;line-height:21px}
.promo-sub{font-family:"Ropa Sans",sans-serif;color:var(--orange);font-size:15px;line-height:18px}
.promo-text{font-size:10.5px;line-height:15px;color:var(--text-soft);margin-top:8px}
.btn-orange{display:inline-block;margin-top:8px;background:var(--orange);color:var(--white);font-size:11.5px;padding:4px 9px;border-radius:4px}

.card{position:absolute;top:480px;height:400px;border:1px solid var(--line);border-radius:5px;background:var(--white)}
.card-title{font-family:"Ropa Sans",sans-serif;font-size:20px;padding:8px 15px;border-bottom:1px solid var(--line)}
.card-title.green{color:var(--green)}
.videos{left:11px;width:205px}
.video-thumb{position:absolute;left:6px;width:196px;height:136px;border-radius:3px;display:flex;align-items:center;justify-content:center}
.play{width:38px;height:38px;border-radius:50%;background:rgba(40,40,40,.85);display:flex;align-items:center;justify-content:center}

.welcome{left:225px;width:483px;padding:16px 16px}
.welcome h1{font-family:"Ropa Sans",sans-serif;font-weight:400;font-size:20px;line-height:24px;color:var(--heading);margin-bottom:8px}
.welcome p{font-size:10px;line-height:18px;color:var(--text-soft);hyphens:auto;-webkit-hyphens:auto}
.gap{height:18px}
.btn-gray{display:inline-flex;align-items:center;gap:12px;margin-top:12px;border:1px solid #ccc;border-radius:5px;background:linear-gradient(#fafafa,#e9e9e9);padding:6px 14px;font-size:12px;color:#444;text-decoration:underline}

.testimonials{left:718px;width:265px}
.quote{padding:0 16px;font-size:10px;line-height:18px;color:var(--text-soft);hyphens:auto;-webkit-hyphens:auto}
.author{display:flex;justify-content:flex-end;align-items:center;gap:6px;padding-right:26px;font-family:"Ropa Sans",sans-serif;font-size:14px;color:#222;margin:8px 0 20px}

.login-band{position:absolute;left:10px;top:895px;width:970px;height:81px;background:var(--panel);border:1px solid #e4e4e4;font-family:"Ropa Sans",sans-serif;font-size:15.5px;line-height:25px;color:#333;text-align:center;padding-top:14px}

.footer{position:absolute;left:5px;top:990px;width:994px;height:210px;background:var(--panel);border:1px solid #e4e4e4}
.footer h2{font-family:"Ropa Sans",sans-serif;font-weight:400;font-size:17px;color:#222}
.quick{position:absolute;left:20px;top:20px}
.quick-grid{display:grid;grid-template-columns:145px 152px 110px;row-gap:9px;margin-top:16px;font-size:11.5px;color:#333}
.quick-grid span::before{content:"";display:inline-block;border-left:5px solid #999;border-top:4px solid transparent;border-bottom:4px solid transparent;margin-right:8px}
.divider{position:absolute;top:0;width:1px;height:128px;background:#ccc}
.connect{position:absolute;left:468px;top:20px}
.social{display:flex;gap:6px;margin-top:16px}
.social span{width:25px;height:25px;border-radius:3px;background:#3b82c4}
.contact{position:absolute;left:642px;top:20px;font-size:11px}
.contact div{margin-top:12px}
.contact b{font-weight:400;font-size:14px;color:#222;margin-left:3px}
.footer-rule{position:absolute;left:22px;top:165px;width:968px;height:1px;background:#ccc}
.copyright{position:absolute;right:12px;top:180px;font-size:10px;color:#333}
</style>
</head>
<body>
<div class="top-band"></div>

<div class="brand">
  <div class="brand-mark"></div>
  <div>
    <div class="brand-name">Peartreegrove</div>
    <div class="brand-tagline">BALANCED NUTRITION, MIND, AND FITNESS</div>
  </div>
</div>

<div class="search">
  <span>Enter keyword</span>
  <svg width="18" height="18" viewBox="0 0 18 18"><circle cx="7" cy="7" r="5" fill="none" stroke="#999" stroke-width="2"/><line x1="11" y1="11" x2="16" y2="16" stroke="#999" stroke-width="3" stroke-linecap="round"/></svg>
</div>

<nav class="main-nav">
  <a style="width:136px">Your Coaching Program</a>
  <a style="width:120px">Why a Health Coach</a>
  <a style="width:101px">About Your Coach</a>
  <a style="width:78px">Recipe</a>
  <a style="width:131px">Body &amp; Mind Workouts</a>
</nav>

<section class="hero" role="img" aria-label="Photo of a man stretching in a lunge on a sunny beach by the sea">
  <div class="hero-caption head-font">
    <span>Excersice tittle line goes here</span>
    <div class="hero-dots"><span></span><span></span><span></span><span></span></div>
  </div>
</section>

<aside class="promo" style="top:154px">
  <div class="promo-photo" role="img" aria-label="Photo of a boy holding a fruit above plates of fresh vegetables and fruit" style="background:linear-gradient(#f4efe6,#c9d39a)"></div>
  <div class="promo-body">
    <div class="promo-title">BEST NUTRITION</div>
    <div class="promo-sub">AND DIET</div>
    <p class="promo-text">We can assure you that this is the best place for requirement of yours regarding</p>
    <span class="btn-orange">learn more</span>
  </div>
</aside>

<aside class="promo" style="top:315px">
  <div class="promo-photo" role="img" aria-label="Photo of a smiling fitness woman holding fresh green leaves" style="background:linear-gradient(#f1f1f1,#8c8076)"></div>
  <div class="promo-body">
    <div class="promo-title">BODY FITNESS</div>
    <div class="promo-sub">AND EXCERCISE</div>
    <p class="promo-text">We can assure you that this is the best place for requirement of yours regarding</p>
    <span class="btn-orange">learn more</span>
  </div>
</aside>

<section class="card videos">
  <div class="card-title green">Our Videos</div>
  <div class="video-thumb" style="top:44px;background:linear-gradient(#f3d2b8,#d9a07a)" role="img" aria-label="Video still of children doing cartwheels on a beach">
    <div class="play"><svg width="14" height="16" viewBox="0 0 14 16"><path d="M2 1 L13 8 L2 15 Z" fill="#fff"/></svg></div>
  </div>
  <div class="video-thumb" style="top:190px;background:linear-gradient(#6b9fda,#b3c9e4)" role="img" aria-label="Video still of a woman with outstretched arms under a blue sky">
    <div class="play"><svg width="14" height="16" viewBox="0 0 14 16"><path d="M2 1 L13 8 L2 15 Z" fill="#fff"/></svg></div>
  </div>
</section>

<section class="card welcome">
  <h1>Welcome to Our Webste Mainpage</h1>
  <p>Brightfield Webworks provides you the Search Engine Optimization making your website search engine friendly. So that the website can achieve top position and ranking in the Internet searches and thereby increasing the scope for the website to be found by customers. We here modify the site to improve the ranking by using the keywords and contents.</p>
  <div class="gap"></div>
  <p>E-Commerce is a major progress in technology that has changed the way in which the customers now purchase information, products and the services. It’s the new way of providing an opportunity to make your products and services available in the global market 24 hours a day through Internet</p>
  <p>Brightfield Webworks is specialized in handling advanced web projects and the ongoing projects that require permanent maintenance and support .We like challenges and do complete these challenge with expertise we like solving questions that arises in such projects as these helps us to grow also.</p>
  <p>Static website is a simple way to get your message out to the public. Static website are cheaper and also it needs less maintenance too. It’s the simplest, cheapest and also the basic thing the search engine picks it up very easily.</p>
  <span class="btn-gray">Contact your health coach <svg width="6" height="9" viewBox="0 0 6 9"><path d="M0 0 L6 4.5 L0 9 Z" fill="#999"/></svg></span>
</section>

<section class="card testimonials">
  <div class="card-title green" style="margin-bottom:12px">Testimonials</div>
  <p class="quote">Brightfield Webworks is specialized in handling advanced web projects and the ongoing projects that require permanent maintenance and support .We like challenges and do complete these challenge with expertise we like solving questions that arises in such projects as these helps us to grow also.</p>
  <div class="author"><svg width="32" height="12" viewBox="0 0 32 12"><path d="M1 3 Q14 10 30 7" fill="none" stroke="#222" stroke-width="1.5"/><path d="M25 3 L31 7 L25 10" fill="none" stroke="#222" stroke-width="1.5"/></svg>By Author Name</div>
  <p class="quote">Static website are cheaper and also it needs less maintenance too. It’s the simplest, cheapest and also the basic thing the search engine picks it up very easily.</p>
  <p class="quote" style="margin-top:6px">We at Brightfield provide you the best simple websites too with total work done as using all the best designing and all done</p>
  <div class="author"><svg width="32" height="12" viewBox="0 0 32 12"><path d="M1 3 Q14 10 30 7" fill="none" stroke="#222" stroke-width="1.5"/><path d="M25 3 L31 7 L25 10" fill="none" stroke="#222" stroke-width="1.5"/></svg>By Author Name</div>
</section>

<div class="login-band">
  Client login: get your free login to access to monthly newsletter and archived articles (anyone) as well as teleconferences –<br>
  to access videos , that privilege is for clients only (please submit your e-mail address and client Number) – thanks!
</div>

<footer class="footer">
  <div class="quick">
    <h2>Quick Links</h2>
    <div class="quick-grid">
      <span>Home</span><span>About Your Coach</span><span>Testimonials</span>
      <span>About Us</span><span>Recipe</span><span>Videos</span>
      <span>Why Health Coach</span><span>Body &amp; Mind Workouts</span><span>Blog</span>
    </div>
  </div>
  <div class="divider" style="left:438px"></div>
  <div class="connect">
    <h2>Stay Connected</h2>
    <div class="social" aria-label="Social network links">
      <span style="background:#4ab0e6"></span><span style="background:#2a6fb0"></span><span style="background:#3b5fa8"></span>
    </div>
  </div>
  <div class="divider" style="left:608px"></div>
  <div class="contact">
    <h2>Contact Info</h2>
    <div>Email: <b>mara@peartreegrove.example</b></div>
    <div>Phone: <b style="font-size:15px">407-555-0186</b></div>
  </div>
  <div class="footer-rule"></div>
  <div class="copyright">© 2012 Company Name &nbsp;|&nbsp; Al right reserved &nbsp;|&nbsp; Term &amp; Conditions</div>
</footer>
</body>
</html>
```